Kitchen construction business needs a flyer

We are a new business and are in need a flyer designed to help launch our products. We build all internal and external joinery, custom kitchens and bathroom products, laundries, robes, home office and other custom joinery.
Must state that we offer builders a discount of our services.
Contact details
Office Phone 02 47365208
Mobile Phone 0418653027
Website Bramblewoodcabinetry.com.au
Email bramblewoodcabinetry@mailpost.com

Target Market(s)

Builders, renovators, commercial and residential

Requirements
Must have
• Must state discount for builders
• Competition time, like our Friendlink page or Photoloop page and tag a friend to go into the draw to win a free laundry. Conditions apply
• We are on Friendlink and Photoloop

```html
<!DOCTYPE html>
<html lang="en">
<head>
<meta charset="utf-8">
<title>Bramblewood Cabinetry – Flyer</title>
<link href="https://fonts.googleapis.com/css2?family=Ubuntu:wght@400;500;700&family=Open+Sans:wght@400;600&display=swap" rel="stylesheet">
<style>
  :root{
    --blue:#3a8ad3;
    --blue-deep:#2c6fb5;
    --navy:#2f3a48;
    --ink:#2a2f36;
    --white:#ffffff;
    --canvas:#e4e4e4;
  }
  *{box-sizing:border-box;margin:0;padding:0}
  html,body{width:1200px;height:1200px;overflow:hidden;background:var(--canvas)}
  body{font-family:"Ubuntu",sans-serif;color:var(--ink)}
  .sheets{position:absolute;left:231px;top:48px;width:921px;transform:scale(.8);transform-origin:0 0}
  .panel{position:relative;width:921px;height:650px;background:var(--white);overflow:hidden;box-shadow:0 2px 6px rgba(0,0,0,.25)}
  .panel--inside{margin-top:62px;height:652px}
  .abs{position:absolute}
  .photo{position:absolute}

  /* outside panel */
  .photo--bathroom{left:0;top:0;width:307px;height:392px;background:linear-gradient(160deg,#e8e6e3 0%,#cfc9c2 55%,#a4825e 100%)}
  .photo--kitchen{left:307px;top:0;width:614px;height:392px;background:linear-gradient(180deg,#f2f1ef 0%,#dcdad6 50%,#bdb6ad 100%)}
  .kitchen-tint{left:0;top:0}
  .brand{left:620px;top:0;width:250px;height:145px;background:var(--white);display:flex;align-items:center;justify-content:center;gap:10px}
  .brand__mark{width:14px;height:14px;background:var(--blue-deep)}
  .brand__name{font-size:20px;font-weight:500;color:var(--blue-deep);line-height:1.15;letter-spacing:.04em;text-transform:uppercase}
  .inset-frame{left:74px;top:318px;width:158px;height:150px;border:6px solid var(--blue-deep);border-top:none}
  .photo--table{left:86px;top:328px;width:134px;height:132px;background:linear-gradient(170deg,#e9e6e1 0%,#c9b69d 55%,#7a5434 100%);border:2px solid var(--white)}
  .products{left:62px;top:488px;width:240px}
  .products__title{font-size:22px;font-weight:700;color:var(--navy);padding-bottom:5px;border-bottom:3px solid var(--blue);display:inline-block;letter-spacing:.02em}
  .products__list{list-style:none;margin-top:16px;font-family:"Open Sans",sans-serif;font-size:13.5px;line-height:17.5px}
  .products__list li{position:relative;padding-left:16px}
  .tick{position:absolute;left:0;top:3px;width:11px;height:11px}
  .contact{left:307px;top:392px;width:306px;height:258px;background:var(--navy);color:var(--white);text-align:center}
  .contact__title{margin-top:16px;font-size:24px;font-weight:500;letter-spacing:.2em}
  .contact__phones{margin-top:10px;font-size:21px;font-weight:500;letter-spacing:.05em;line-height:29px}
  .contact__phones span{display:inline-flex;align-items:center;gap:12px}
  .rule{height:2px;background:var(--blue);margin:0 18px}
  .contact__web{padding:9px 0 8px;font-family:"Open Sans",sans-serif;font-weight:600;font-size:14px;line-height:19px}
  .follow{font-size:21px;font-weight:500;margin-top:9px}
  .social{display:flex;justify-content:center;gap:8px;margin-top:4px}
  .social i{width:25px;height:25px;border-radius:50%;background:var(--blue-deep);display:block}
  .social i+i{background:#c2416c}
  .pitch{left:627px;top:440px;width:290px}
  .pitch__big{font-size:56px;font-weight:700;line-height:1;color:var(--ink)}
  .pitch__line{font-size:20px;font-weight:700;line-height:28px;color:var(--ink);display:flex;align-items:center;gap:12px}
  .pitch__line::after{content:"";flex:1;height:3px;background:var(--blue-deep)}
  .pitch__line--last::after{display:none}
  .webband{left:613px;top:590px;width:308px;height:60px;background:var(--blue);color:var(--white);font-size:18px;font-weight:500;display:flex;align-items:center;justify-content:center}

  /* inside panel */
  .photo--island{left:0;top:0}
  .offer{left:0;top:0}
  .offer__text{left:0;top:22px;width:307px;text-align:center;color:var(--white)}
  .offer__lead{font-size:28px;font-weight:500}
  .offer__big{font-size:62px;font-weight:700;line-height:1;margin-top:2px}
  .offer__tail{font-size:33px;font-weight:700;line-height:1.1}
  .offer__ids{left:0;top:220px;width:307px;text-align:center;color:var(--white);font-size:18px;font-weight:700;line-height:24px}
  .compete{left:322px;top:22px;width:278px;text-align:center}
  .compete__title{font-size:29px;font-weight:400;color:var(--blue)}
  .compete__body{margin-top:16px;font-family:"Open Sans",sans-serif;font-size:17.5px;line-height:23.5px;color:var(--ink)}
  .compete__note{font-family:"Open Sans",sans-serif;font-size:11.5px}
  .framed{border:10px solid rgba(255,255,255,.75);border-bottom-color:var(--blue-deep)}
  .framed__photo{width:100%;height:100%;background:linear-gradient(160deg,#c9c4bb 0%,#8c7a66 50%,#2c2926 100%)}
  .framed--upper{left:675px;top:60px;width:187px;height:186px}
  .framed--lower{left:368px;top:240px;width:187px;height:186px}
  .footer{left:0;top:585px;width:921px;height:67px;background:var(--navy);color:var(--white);font-size:14.5px;font-weight:700;line-height:19px}
  .footer__col{position:absolute;top:12px}
  .footer__col span{display:flex;align-items:center;gap:9px}
  .footer__col svg{width:17px;height:15px}
  .footer__follow{left:708px;top:8px;width:110px;text-align:center;font-size:14.5px}
  .footer__follow .social{margin-top:5px}
  .footer__follow .social i{width:22px;height:22px}
</style>
</head>
<body>
<div class="sheets">

  <section class="panel panel--outside">
    <div class="photo photo--bathroom" role="img" aria-label="Bathroom with timber vanity, toilet and window"></div>
    <div class="photo photo--kitchen" role="img" aria-label="White kitchen with island bench, pendant light and bar stools"></div>
    <svg class="abs kitchen-tint" width="921" height="392" viewBox="0 0 921 392" aria-hidden="true">
      <polygon points="880,0 921,0 921,392 770,392" fill="#2f8bef" opacity=".75"/>
    </svg>
    <div class="abs brand"><span class="brand__mark"></span><span class="brand__name">Bramblewood<br>Cabinetry</span></div>
    <div class="abs inset-frame"></div>
    <div class="photo photo--table" role="img" aria-label="Timber-topped white island table"></div>

    <div class="abs products">
      <h3 class="products__title">OUR PRODUCTS</h3>
      <ul class="products__list">
        <li><svg class="tick" viewBox="0 0 11 11"><rect x=".5" y=".5" width="10" height="10" fill="none" stroke="#3a8ad3"/><path d="M2.5 5.5l2 2 4-5" fill="none" stroke="#3a8ad3" stroke-width="1.4"/></svg>Custom Kitchens<br>and Bathroom products</li>
        <li><svg class="tick" viewBox="0 0 11 11"><rect x=".5" y=".5" width="10" height="10" fill="none" stroke="#3a8ad3"/><path d="M2.5 5.5l2 2 4-5" fill="none" stroke="#3a8ad3" stroke-width="1.4"/></svg>Laundries</li>
        <li><svg class="tick" viewBox="0 0 11 11"><rect x=".5" y=".5" width="10" height="10" fill="none" stroke="#3a8ad3"/><path d="M2.5 5.5l2 2 4-5" fill="none" stroke="#3a8ad3" stroke-width="1.4"/></svg>Robes</li>
        <li><svg class="tick" viewBox="0 0 11 11"><rect x=".5" y=".5" width="10" height="10" fill="none" stroke="#3a8ad3"/><path d="M2.5 5.5l2 2 4-5" fill="none" stroke="#3a8ad3" stroke-width="1.4"/></svg>Home office</li>
        <li><svg class="tick" viewBox="0 0 11 11"><rect x=".5" y=".5" width="10" height="10" fill="none" stroke="#3a8ad3"/><path d="M2.5 5.5l2 2 4-5" fill="none" stroke="#3a8ad3" stroke-width="1.4"/></svg>Other custom joinery</li>
      </ul>
    </div>

    <div class="abs contact">
      <h3 class="contact__title">Contact Details</h3>
      <div class="contact__phones">
        <span><svg width="24" height="20" viewBox="0 0 24 20"><path d="M2 7c0-3 4-5 10-5s10 2 10 5l-4 1-1-2H7L6 8z" fill="#3a8ad3"/><rect x="5" y="10" width="14" height="9" rx="2" fill="#3a8ad3"/></svg>02 47365208</span><br>
        <span><svg width="22" height="22" viewBox="0 0 22 22"><path d="M5 3l3 4-2 2c1 3 3 5 6 6l2-2 4 3-2 3C9 19 3 13 3 5z" fill="#3a8ad3"/></svg>0418653027</span>
      </div>
      <div class="rule" style="margin-top:12px"></div>
      <p class="contact__web">bramblewoodcabinetry@mailpost.com<br>bramblewoodcabinetry.com.au</p>
      <div class="rule"></div>
      <p class="follow">Follow us on</p>
      <div class="social"><i></i><i></i></div>
    </div>

    <div class="abs pitch">
      <p class="pitch__big">WE BUILD</p>
      <p class="pitch__line" style="margin-top:6px">ALL INTERNAL</p>
      <p class="pitch__line pitch__line--last">AND EXTERNAL JOINERY</p>
    </div>
    <div class="abs webband">bramblewoodcabinetry.com.au</div>
  </section>

  <section class="panel panel--inside">
    <svg class="abs photo--island" width="921" height="585" viewBox="0 0 921 585" role="img" aria-label="Kitchen with granite island bench, steel fridge and white cabinets">
      <defs>
        <linearGradient id="island" x1="0" y1="0" x2="0" y2="1">
          <stop offset="0" stop-color="#e9e8e5"/><stop offset=".6" stop-color="#c9c5bf"/><stop offset="1" stop-color="#4a3a2e"/>
        </linearGradient>
      </defs>
      <polygon points="880,0 921,0 921,585 200,585" fill="url(#island)"/>
      <polygon points="615,0 880,0 615,228" fill="#2f3a48"/>
    </svg>
    <svg class="abs offer" width="307" height="585" viewBox="0 0 307 585" role="img" aria-label="Faded blue-tinted kitchen">
      <defs>
        <linearGradient id="offerfade" x1="0" y1="0" x2="0" y2="1">
          <stop offset="0" stop-color="#3a8ad3"/><stop offset=".55" stop-color="#4a93d6"/><stop offset="1" stop-color="#6aa6dc"/>
        </linearGradient>
      </defs>
      <polygon points="0,0 307,0 307,493 200,585 0,585" fill="url(#offerfade)"/>
    </svg>
    <div class="abs offer__text">
      <p class="offer__lead">we offer builders a</p>
      <p class="offer__big">discount</p>
      <p class="offer__tail">of our services</p>
    </div>
    <p class="abs offer__ids">ABN 58 402 913 227<br>LIC 417230B</p>

    <div class="abs compete">
      <h2 class="compete__title">Competition time</h2>
      <p class="compete__body">Like our Friendlink page or Photoloop page and tag a friend to go into the draw to win a free laundry.</p>
      <p class="compete__note">Conditions apply *</p>
    </div>

    <div class="abs framed framed--upper"><div class="framed__photo" role="img" aria-label="Dark benchtop with fruit bowl and timber shelves"></div></div>
    <div class="abs framed framed--lower"><div class="framed__photo" role="img" aria-label="Dark benchtop with fruit bowl and timber shelves"></div></div>

    <footer class="abs footer">
      <div class="footer__col" style="left:95px">
        <span><svg viewBox="0 0 24 20"><path d="M2 7c0-3 4-5 10-5s10 2 10 5l-4 1-1-2H7L6 8z" fill="#3a8ad3"/><rect x="5" y="10" width="14" height="9" rx="2" fill="#3a8ad3"/></svg>02 47365208</span>
        <span><svg viewBox="0 0 22 22"><path d="M5 3l3 4-2 2c1 3 3 5 6 6l2-2 4 3-2 3C9 19 3 13 3 5z" fill="#3a8ad3"/></svg>0418653027</span>
      </div>
      <div class="footer__col" style="left:320px">
        <span><svg viewBox="0 0 16 16"><circle cx="8" cy="8" r="6.5" fill="none" stroke="#3a8ad3" stroke-width="1.5"/><ellipse cx="8" cy="8" rx="3" ry="6.5" fill="none" stroke="#3a8ad3" stroke-width="1.2"/><path d="M1.5 8h13" stroke="#3a8ad3" stroke-width="1.2"/></svg>bramblewoodcabinetry.com.au</span>
        <span><svg viewBox="0 0 18 14"><rect x="1" y="1" width="16" height="12" rx="1" fill="#3a8ad3"/><path d="M1 2l8 6 8-6" fill="none" stroke="#2f3a48" stroke-width="1.4"/></svg>bramblewoodcabinetry@mailpost.com</span>
      </div>
      <div class="footer__col footer__follow">Follow us on<div class="social"><i></i><i></i></div></div>
    </footer>
  </section>

</div>
</body>
</html>
```